Innovative Strategic IT Solutions and Management Consulting

Looking for a fresh design idea to represent a company which specializes in innovative strategic IT solutions focusing on information assurance, enterprise content management, health information technology, web applications, strategic IT solutions and solutions architect.

KELTO...the company name means "new beginning" in Greek or the acronym for Keep-Every-Layer-Tightly-Organized. We pride ourselves in understanding the client's business and needs before proposing an innovative solutions.

Innovation / Secure / Strategy - the core motto

Color: Maroon / Burgundy / Silver / White / Grey / Black

Primary focus color: Burgundy / Silver

```html
<!DOCTYPE html>
<html lang="en">
<head>
<meta charset="utf-8">
<title>KELTO – Innovative Strategic IT Solutions</title>
<link rel="stylesheet" href="https://fonts.googleapis.com/css2?family=Source+Sans+3:wght@300;400;600&display=swap">
<style>
:root{
  --burgundy:#4e1218;
  --maroon:#531009;
  --red:#9a0d0d;
  --button:#8a0c0c;
  --silver:#f1eff0;
  --ink:#3a3a3a;
  --white:#ffffff;
  --rule:#d9534f;
}
*{margin:0;padding:0;box-sizing:border-box}
html,body{width:1093px;height:1200px;overflow:hidden;background:var(--white)}
body{position:relative;font-family:"Source Sans 3",sans-serif;color:var(--ink)}
.abs{position:absolute}

.brand{left:66px;top:26px;font-size:38px;font-weight:600;color:#8a0f14;letter-spacing:1px;line-height:1}
.nav{top:40px;font-size:13px;color:#444;text-transform:uppercase}
.nav.active::before{content:"";position:absolute;left:3px;right:3px;top:-8px;height:2px;background:var(--rule)}

.hero{left:64px;top:64px;width:963px;height:534px;
  background:linear-gradient(180deg,#d9d5cf 0%,#9a928a 35%,#5a5450 65%,#3b3a3c 100%)}
.hero-title{left:64px;width:963px;top:218px;text-align:center;color:#fff;font-size:37px;font-weight:400;letter-spacing:0.5px}
.hero-sub{left:64px;width:963px;top:278px;text-align:center;color:#fff;font-size:18px}
.hero-body{left:330px;width:430px;top:323px;text-align:center;color:#fff;font-size:14.5px;font-weight:300;line-height:19px}
.hero-btn{left:485px;top:412px;width:122px;height:49px;border:2px solid #fff;color:#fff;font-size:15px;font-weight:300;display:flex;align-items:center;justify-content:center}
.arrow{top:378px}

.band{left:0;top:598px;width:1093px;height:68px;background:var(--burgundy)}
.band-item{top:622px;color:#fff;font-size:16px;display:flex;align-items:center;gap:10px}

.features{left:0;top:666px;width:1093px;height:339px;background:var(--silver)}
.feature{width:260px;text-align:center}
.feature h2{font-size:19px;font-weight:400;color:var(--red);margin-bottom:6px}
.feature p{font-size:11.5px;line-height:15.3px;color:#444}
.read{width:120px;height:40px;background:var(--button);color:#fff;font-size:16px;display:flex;align-items:center;justify-content:center;box-shadow:2px 2px 3px rgba(0,0,0,.35);top:930px}

.footer{left:0;top:1005px;width:1093px;height:195px;background:var(--maroon)}
.foot-head{top:1047px;color:#fff;font-size:24px;font-weight:300}
.foot-links{top:1092px;color:#fff;font-size:14px;line-height:26.3px;list-style:none}
.social{left:474px;top:1095px;display:flex;gap:10px}
</style>
</head>
<body>

<div class="abs brand">KELTO</div>
<div class="abs nav active" style="left:559px">Home</div>
<div class="abs nav" style="left:638px">Solutions</div>
<div class="abs nav" style="left:746px">Strategy</div>
<div class="abs nav" style="left:846px">Security</div>
<div class="abs nav" style="left:942px">Technologies</div>

<div class="abs hero" role="img" aria-label="Photo of business people meeting around a conference table"></div>
<h1 class="abs hero-title">INNOVATIVE STRATEGIC IT SOLUTIONS</h1>
<div class="abs hero-sub">Build/develop Custum website and Web Application</div>
<p class="abs hero-body">Web Development offers professional Website development services to help you successfully plan, create,&nbsp; maintain and market your Web development project.</p>
<div class="abs hero-btn">LEARN MORE</div>
<svg class="abs arrow" style="left:86px" width="12" height="46" viewBox="0 0 12 46"><path d="M10 2 Q0 23 10 44" fill="none" stroke="#fff" stroke-width="3"/></svg>
<svg class="abs arrow" style="left:990px" width="12" height="46" viewBox="0 0 12 46"><path d="M2 2 Q12 23 2 44" fill="none" stroke="#fff" stroke-width="3"/></svg>

<div class="abs band"></div>
<div class="abs band-item" style="left:66px">
  <svg width="18" height="18" viewBox="0 0 18 18"><rect x="1" y="3" width="13" height="13" rx="2" fill="none" stroke="#fff" stroke-width="2"/><path d="M7 11 L16 2" stroke="#fff" stroke-width="2.5"/></svg>Solutions Architect</div>
<div class="abs band-item" style="left:324px">
  <svg width="16" height="18" viewBox="0 0 16 18"><rect x="1" y="1" width="14" height="16" fill="none" stroke="#fff" stroke-width="1.6"/><rect x="1" y="1" width="14" height="4" fill="#fff"/><path d="M6 9 L4 11.5 L6 14 M10 9 L12 11.5 L10 14" fill="none" stroke="#fff" stroke-width="1.2"/></svg>Strategic Management</div>
<div class="abs band-item" style="left:622px">
  <svg width="18" height="18" viewBox="0 0 18 18"><rect x="1" y="1" width="10" height="14" fill="none" stroke="#fff" stroke-width="1.6"/><circle cx="12" cy="12" r="4.5" fill="#fff"/></svg>Application Development</div>
<div class="abs band-item" style="left:923px">
  <svg width="16" height="18" viewBox="0 0 16 18"><rect x="1" y="3" width="14" height="14" fill="none" stroke="#fff" stroke-width="1.6"/><rect x="4" y="0.5" width="8" height="3" fill="#fff"/><path d="M8 7 V14 M4.5 10.5 H11.5" stroke="#fff" stroke-width="2.4"/></svg>Health IT</div>

<div class="abs features"></div>

<svg class="abs" style="left:159px;top:698px" width="96" height="96" viewBox="0 0 96 96">
  <circle cx="48" cy="48" r="44" fill="#fff" stroke="#111" stroke-width="7"/>
  <rect x="22" y="30" width="52" height="34" rx="3" fill="none" stroke="#111" stroke-width="6"/>
  <rect x="44" y="64" width="8" height="8" fill="#111"/><rect x="36" y="71" width="24" height="4" fill="#111"/>
  <path d="M38 56 L66 24" stroke="#111" stroke-width="5"/></svg>
<svg class="abs" style="left:494px;top:698px" width="96" height="96" viewBox="0 0 96 96">
  <circle cx="48" cy="48" r="44" fill="#fff" stroke="#111" stroke-width="7"/>
  <rect x="32" y="20" width="32" height="10" rx="2" fill="#111"/>
  <rect x="30" y="30" width="36" height="44" rx="4" fill="none" stroke="#111" stroke-width="6"/>
  <path d="M48 42 V62 M38 52 H58" stroke="#111" stroke-width="7"/></svg>
<svg class="abs" style="left:857px;top:710px" width="72" height="84" viewBox="0 0 72 84">
  <path d="M6 8 L36 2 L66 8 L68 56 Q60 76 36 82 Q12 76 4 56 Z" fill="#1a1a1a" stroke="#9a9a9a" stroke-width="3"/>
  <path d="M27 40 V30 A9 9 0 0 1 45 30" fill="none" stroke="#fff" stroke-width="4"/>
  <rect x="24" y="40" width="24" height="20" rx="2" fill="#fff"/><rect x="34" y="45" width="4" height="9" fill="#1a1a1a"/></svg>

<div class="abs feature" style="left:79px;top:806px">
  <h2>Innovative Solutions</h2>
  <p>We create meaningful websites that offersimplistic user experiences, achieve highr ankings on the mo st popular search engines and promote your bran dto the wides tossible audience.</p>
</div>
<div class="abs feature" style="left:407px;top:808px;width:276px">
  <h2 style="margin-bottom:10px">Health IT</h2>
  <p>Our emphasis on quality code and our straight-forward approach to custom web solutions will streamline your operations. We focus on scalable development to ensur e pain-free maintenance and application longevity.</p>
</div>
<div class="abs feature" style="left:753px;top:807px;width:250px">
  <h2 style="margin-bottom:3px">Information Assurance</h2>
  <p>Our Internet marketing and content expertswork closely with clients to maximize their online prese-nce. Obtain top rankings for desired search terms and drive qualified leads that are crucial to buil ding your business and brand.</p>
</div>

<div class="abs read" style="left:147px">Read More</div>
<div class="abs read" style="left:481px">Read More</div>
<div class="abs read" style="left:831px">Read More</div>

<div class="abs footer"></div>
<div class="abs foot-head" style="left:65px">Services</div>
<ul class="abs foot-links" style="left:66px">
  <li>Solutions Architect</li><li>Strategic Management</li><li>Application Development</li><li>Health IT</li></ul>
<div class="abs foot-head" style="left:265px">About Us</div>
<ul class="abs foot-links" style="left:266px">
  <li>Company Profile</li><li>Our Team</li><li>Company Culture</li></ul>
<div class="abs foot-head" style="left:474px">Stay Connected</div>
<div class="abs social" aria-label="Social links">
  <svg width="28" height="28"><circle cx="14" cy="14" r="12.5" fill="none" stroke="#fff" stroke-width="2"/></svg>
  <svg width="28" height="28"><circle cx="14" cy="14" r="12.5" fill="none" stroke="#fff" stroke-width="2"/></svg>
  <svg width="28" height="28"><circle cx="14" cy="14" r="12.5" fill="none" stroke="#fff" stroke-width="2"/></svg>
  <svg width="28" height="28"><circle cx="14" cy="14" r="12.5" fill="none" stroke="#fff" stroke-width="2"/></svg>
</div>
<div class="abs foot-head" style="left:754px">Blog</div>
<ul class="abs foot-links" style="left:755px;line-height:28px">
  <li>Construct An</li><li>IT Solution.</li></ul>
<div class="abs foot-head" style="left:925px">Legal Stuff</div>
<p class="abs foot-links" style="left:926px;line-height:19.5px;width:110px">© 2014 KELTO IT solutions . All Rights Reserved</p>

</body>
</html>
```